Birchway Cleaning Commercial Flyer

Would like a flyer that will be used for making sales calls for commercial clients. These flyers will be handed out to Business Owners and facility managers. The flyer must peak interest, introduce the company, and give some information about our services. Birchway Cleaning Services (BWS) is a modern company that is eco-friendly. I have added what the uniform shirt looks like we have one in orange and one in blue. It would be nice to see the pictures you choose have the uniform on.

Target Market(s)

Office Mangers and Facility managers

Industry/Entity Type

Office Cleaning

Font styles to use
Serif

Colors
f78f20
0355a3
abd037

Requirements
Must have
• Modern clean look and feel. The flyer must straight forward and not busy.
• Have sections where bullet points or other written information can be placed
• Must be able to add and move information myself after the design has been decided on.
• Have a section that says:
• To learn more call 301-555-0148 or email info@birchway-tidyworks.example
Nice to have
• Some pictures, clean and modern. Peak interest. The uniform to be photoshopped onto the models of the pictures
Should not have
• too busy

```html
<!DOCTYPE html>
<html lang="en">
<head>
<meta charset="utf-8">
<title>Birchway Cleaning Commercial Flyer</title>
<link href="https://fonts.googleapis.com/css2?family=Oswald:wght@400;500;600;700&family=Roboto+Condensed:wght@400;700&family=Roboto:wght@400;500&display=swap" rel="stylesheet">
<style>
  :root {
    --brand-blue: #0a63b0;
    --deep-blue: #0355a3;
    --brand-orange: #f78f20;
    --brand-green: #abd037;
    --seal-green: #3fa535;
    --offer-red: #e32726;
    --ink: #1c1c1c;
    --page-bg: #ebebeb;
    --paper: #ffffff;
    --paper-tint: #e6f0f8;
  }
  * { box-sizing: border-box; margin: 0; padding: 0; }
  html, body { width: 1200px; height: 858px; overflow: hidden; }
  body { background: var(--page-bg); font-family: "Roboto", Arial, sans-serif; color: var(--ink); position: relative; }

  .flyer {
    position: absolute; left: 300px; top: 37px; width: 600px; height: 784px;
    background: linear-gradient(180deg, var(--paper) 50%, var(--paper-tint) 100%);
    overflow: hidden; box-shadow: 0 18px 30px rgba(0,0,0,0.18);
  }
  .hero-photo { position: absolute; left: 0; top: 0; width: 600px; height: 430px; }
  .hero-swoosh { position: absolute; left: 0; top: 340px; width: 600px; height: 100px; }

  .brand { position: absolute; left: 30px; top: 36px; width: 180px; text-align: center; }
  .brand-dot { width: 62px; height: 62px; border-radius: 50%; background: var(--brand-orange); margin: 0 auto 8px; }
  .brand-name { font-family: "Roboto Condensed", sans-serif; font-size: 15px; font-weight: 400; color: var(--brand-blue); white-space: nowrap; }

  .headline { position: absolute; right: 44px; top: 46px; text-align: left; color: var(--brand-blue); }
  .headline-top { font-family: "Oswald", sans-serif; font-weight: 700; font-size: 56px; letter-spacing: 9px; line-height: 1; }
  .headline-mid { font-family: "Roboto Condensed", sans-serif; font-size: 23px; line-height: 1.3; margin-top: 4px; }
  .headline-bottom { font-family: "Oswald", sans-serif; font-weight: 600; font-size: 42px; line-height: 1.1; letter-spacing: 0.5px; }

  .eco-seal { position: absolute; left: 358px; top: 280px; width: 148px; height: 148px; }

  .services { position: absolute; left: 46px; top: 444px; width: 250px; }
  .services-title { font-family: "Oswald", sans-serif; font-weight: 600; font-size: 27px; color: var(--brand-orange); line-height: 1.1; }
  .services-intro { font-size: 11.5px; line-height: 1.55; margin-top: 6px; }
  .services-list { list-style: none; margin-top: 6px; }
  .services-list li { font-size: 11.5px; line-height: 19.6px; display: flex; align-items: center; gap: 5px; }
  .services-list svg { width: 14px; height: 14px; flex: none; }

  .web-button {
    position: absolute; left: 31px; top: 711px; width: 260px; height: 42px;
    background: var(--brand-orange); border-radius: 0 10px 10px 0;
    font-family: "Roboto Condensed", sans-serif; font-weight: 700; font-size: 15px; color: #fff;
    display: flex; align-items: center; justify-content: center;
  }

  .offer { position: absolute; left: 318px; top: 444px; width: 252px; text-align: center; }
  .offer-value { font-family: "Oswald", sans-serif; font-weight: 700; font-size: 50px; color: var(--offer-red); line-height: 1; }
  .offer-note { font-family: "Roboto Condensed", sans-serif; font-size: 18px; margin-top: 4px; }

  .feature-badge { position: absolute; top: 550px; width: 116px; height: 116px; }
  .feature-badge.disinfect { left: 310px; }
  .feature-badge.vacuums { left: 440px; }

  .contact { position: absolute; right: 36px; top: 678px; text-align: right; }
  .contact-lead { font-family: "Roboto Condensed", sans-serif; font-size: 21px; }
  .contact-phone { font-family: "Oswald", sans-serif; font-weight: 600; font-size: 29px; line-height: 1.2; display: flex; align-items: center; justify-content: flex-end; gap: 5px; }
  .contact-phone svg { width: 24px; height: 24px; }
  .contact-email { font-size: 12.5px; display: flex; align-items: center; justify-content: flex-end; gap: 6px; }
  .contact-email svg { width: 20px; height: 14px; }
</style>
</head>
<body>
<main class="flyer">
  <svg class="hero-photo" viewBox="0 0 600 430" role="img" aria-label="Photo of a cleaner in the orange company uniform wiping a window with a green cloth in a bright white office">
    <defs>
      <linearGradient id="room" x1="0" y1="0" x2="1" y2="1">
        <stop offset="0" stop-color="#f4f6f7"/>
        <stop offset="0.55" stop-color="#e7ebee"/>
        <stop offset="1" stop-color="#dfe4e8"/>
      </linearGradient>
      <radialGradient id="figure" cx="0.22" cy="0.75" r="0.35">
        <stop offset="0" stop-color="#f26b1d" stop-opacity="0.85"/>
        <stop offset="1" stop-color="#f26b1d" stop-opacity="0"/>
      </radialGradient>
    </defs>
    <path d="M0 0 H600 V360 Q330 375 0 430 Z" fill="url(#room)"/>
    <path d="M0 0 H600 V360 Q330 375 0 430 Z" fill="url(#figure)"/>
  </svg>
  <svg class="hero-swoosh" viewBox="0 0 600 100" aria-hidden="true">
    <path d="M0 90 Q320 20 600 30 V36 Q320 28 0 98 Z" fill="var(--brand-blue)"/>
  </svg>

  <div class="brand">
    <div class="brand-dot"></div>
    <div class="brand-name">Birchway Cleaning Services</div>
  </div>

  <header class="headline">
    <div class="headline-top">HEALTHY</div>
    <div class="headline-mid">Office/Work Environment is</div>
    <div class="headline-bottom">HAPPY OFFICE</div>
  </header>

  <svg class="eco-seal" viewBox="0 0 148 148" aria-label="Eco-friendly microfiber cloths">
    <circle cx="74" cy="70" r="64" fill="#e9efe4" stroke="#c9d3c2" stroke-width="2" stroke-dasharray="3 3"/>
    <circle cx="74" cy="70" r="54" fill="var(--seal-green)"/>
    <circle cx="74" cy="70" r="54" fill="none" stroke="#2f7f2a" stroke-width="3"/>
    <text x="74" y="62" text-anchor="middle" font-family="Roboto Condensed, sans-serif" font-weight="700" font-size="21" fill="#fff">Eco-</text>
    <text x="74" y="86" text-anchor="middle" font-family="Roboto Condensed, sans-serif" font-weight="700" font-size="21" fill="#fff">Friendly</text>
    <path d="M6 104 L22 96 L126 96 L142 104 L132 110 L142 118 L126 122 L22 122 L6 118 L16 110 Z" fill="#b81f1f"/>
    <rect x="20" y="96" width="108" height="24" fill="var(--offer-red)"/>
    <text x="74" y="113" text-anchor="middle" font-family="Roboto Condensed, sans-serif" font-weight="700" font-size="10.5" fill="#fff">MICROFIBER CLOTHS</text>
  </svg>

  <section class="services">
    <h2 class="services-title">OUR SERVICES</h2>
    <p class="services-intro">Lorem ipsum dolor sit amet, consectetur adipisicing elit, sed do eiusmod tempor incididunt ut labore et dolore magna aliqua.</p>
    <ul class="services-list">
      <li><svg viewBox="0 0 14 14"><path d="M1 7 L5 12 L13 1" fill="none" stroke="var(--seal-green)" stroke-width="2"/></svg>Ut enim ad minim veniam, quis nostrud.</li>
      <li><svg viewBox="0 0 14 14"><path d="M1 7 L5 12 L13 1" fill="none" stroke="var(--seal-green)" stroke-width="2"/></svg>Exercitation ullamco laboris nisi.</li>
      <li><svg viewBox="0 0 14 14"><path d="M1 7 L5 12 L13 1" fill="none" stroke="var(--seal-green)" stroke-width="2"/></svg>Aliquip ex ea commodo consequat.</li>
      <li><svg viewBox="0 0 14 14"><path d="M1 7 L5 12 L13 1" fill="none" stroke="var(--seal-green)" stroke-width="2"/></svg>Duis aute irure dolor in reprehenderit.</li>
      <li><svg viewBox="0 0 14 14"><path d="M1 7 L5 12 L13 1" fill="none" stroke="var(--seal-green)" stroke-width="2"/></svg>Excepteur sint occaecat cupidatat.</li>
      <li><svg viewBox="0 0 14 14"><path d="M1 7 L5 12 L13 1" fill="none" stroke="var(--seal-green)" stroke-width="2"/></svg>Ut enim ad minim veniam, quis nostrud.</li>
      <li><svg viewBox="0 0 14 14"><path d="M1 7 L5 12 L13 1" fill="none" stroke="var(--seal-green)" stroke-width="2"/></svg>Exercitation ullamco laboris nisi.</li>
      <li><svg viewBox="0 0 14 14"><path d="M1 7 L5 12 L13 1" fill="none" stroke="var(--seal-green)" stroke-width="2"/></svg>Excepteur sint occaecat cupidatat.</li>
    </ul>
  </section>

  <div class="web-button">www.birchway-tidyworks.example</div>

  <section class="offer">
    <div class="offer-value">10% OFF</div>
    <div class="offer-note">For the first time services</div>
  </section>

  <svg class="feature-badge disinfect" viewBox="0 0 116 116" aria-label="Hospital grade disinfectants">
    <path d="M40 6 H76 Q86 6 92 14 L104 32 Q110 40 110 50 V66 Q110 76 104 84 L92 102 Q86 110 76 110 H40 Q30 110 24 102 L12 84 Q6 76 6 66 V50 Q6 40 12 32 L24 14 Q30 6 40 6 Z" fill="var(--brand-blue)"/>
    <text x="58" y="46" text-anchor="middle" font-family="Oswald, sans-serif" font-weight="500" font-size="15" fill="#fff">HOSPITAL</text>
    <text x="58" y="71" text-anchor="middle" font-family="Oswald, sans-serif" font-weight="600" font-size="25" fill="#fff">GRADE</text>
    <text x="58" y="88" text-anchor="middle" font-family="Oswald, sans-serif" font-weight="500" font-size="11.5" fill="#fff">DISINFECTANTS</text>
  </svg>

  <svg class="feature-badge vacuums" viewBox="0 0 116 116" aria-label="HEPA backpack vacuums">
    <path d="M40 6 H76 Q86 6 92 14 L104 32 Q110 40 110 50 V66 Q110 76 104 84 L92 102 Q86 110 76 110 H40 Q30 110 24 102 L12 84 Q6 76 6 66 V50 Q6 40 12 32 L24 14 Q30 6 40 6 Z" fill="var(--brand-blue)"/>
    <text x="58" y="52" text-anchor="middle" font-family="Oswald, sans-serif" font-weight="600" font-size="28" fill="#fff">HEPA</text>
    <text x="58" y="71" text-anchor="middle" font-family="Oswald, sans-serif" font-weight="500" font-size="16" fill="#fff">BACKPACK</text>
    <text x="58" y="90" text-anchor="middle" font-family="Oswald, sans-serif" font-weight="500" font-size="17" fill="#fff">VACUUMS</text>
  </svg>

  <section class="contact">
    <div class="contact-lead">To learn more</div>
    <div class="contact-phone">301-555-0148
      <svg viewBox="0 0 24 24" aria-hidden="true"><circle cx="12" cy="12" r="10.5" fill="none" stroke="var(--ink)" stroke-width="1.6"/><path d="M8.5 6.5 L10.5 9 L9.5 10.5 Q10.5 13 13.5 14.5 L15 13.5 L17.5 15.5 L16.5 17.5 Q11 17.5 7 11 Q6.5 8 8.5 6.5 Z" fill="var(--ink)"/></svg>
    </div>
    <div class="contact-email">info@birchway-tidyworks.example
      <svg viewBox="0 0 20 14" aria-hidden="true"><rect width="20" height="14" fill="var(--ink)"/><path d="M0 0 L10 8 L20 0" fill="none" stroke="#fff" stroke-width="1.4"/></svg>
    </div>
  </section>
</main>
</body>
</html>
```